Lorna's Henna Party Invitation on March 20, 2026

I'd like to design an invitation that would be sent via text and posted on social media for my niece's henna party. The color scheme would be white, gold, and black. I want it to be elegant and classy. The font could be something like Rastanty Cortez. The party would be on March 20, 2026. It's a traditional and cultural type of party (pre-wedding party). I've attached some ideas for inspiration and to get a feel of a henna party.

Target Market(s)

This invitation would only be sent via text to our guests and posted on social media.

Font styles to use
Decorative
Script
Other font styles liked:
• Rastanty Cortez

Requirements
Must have
• Elegance, classy, a henna party reflection but something elegant and perhaps abstract.
Nice to have
• Something reflecting the henna party tradition. It could be a high gold candle, a decorated tray, etc. But I want it to be elegant and less crowded of an invitation.

```html
<!DOCTYPE html>
<html lang="en">
<head>
<meta charset="utf-8">
<title>Henna Party Invitation</title>
<link rel="stylesheet" href="https://fonts.googleapis.com/css2?family=Sacramento&family=Noto+Serif&display=swap">
<style>
  :root {
    --paper: #ffffff;
    --ink: #111111;
    --gold: #a8780c;
    --gold-light: #d9b45e;
    --string-tone: #b8975a;
    --string-pale: #efe2c2;
  }
  html, body {
    margin: 0;
    padding: 0;
    overflow: hidden;
    background: var(--paper);
  }
  .invitation {
    position: relative;
    width: 800px;
    height: 1200px;
    overflow: hidden;
    background: var(--paper);
  }
  .henna-motif {
    position: absolute;
    background: radial-gradient(circle at 50% 50%, var(--gold-light) 0%, var(--gold) 70%);
    opacity: 0.85;
  }
  .henna-motif--top-left {
    left: -20px;
    top: -30px;
    width: 230px;
    height: 310px;
    border-radius: 0 0 55% 45%;
  }
  .henna-motif--bottom-right {
    left: 400px;
    top: 968px;
    width: 430px;
    height: 300px;
    border-radius: 55% 50% 0 0;
  }
  .garland {
    position: absolute;
    background: radial-gradient(ellipse at 50% 40%, var(--string-pale) 0%, rgba(239, 226, 194, 0.35) 60%, rgba(255, 255, 255, 0) 100%);
  }
  .garland--top {
    left: 330px;
    top: 0;
    width: 470px;
    height: 270px;
  }
  .garland--bottom {
    left: 0;
    top: 1040px;
    width: 350px;
    height: 160px;
  }
  .script {
    position: absolute;
    left: 0;
    width: 800px;
    margin: 0;
    text-align: center;
    font-family: "Sacramento", cursive;
    color: var(--ink);
    font-size: 50px;
    line-height: 68px;
    font-weight: 400;
  }
  .script--intro { top: 265px; }
  .script--message { top: 612px; left: 30px; width: 740px; }
  .divider-mark {
    position: absolute;
    left: 388px;
    top: 482px;
    width: 24px;
    height: 24px;
    background: var(--gold);
    border-radius: 50%;
    opacity: 0.9;
  }
  .event-date {
    position: absolute;
    left: 0;
    top: 527px;
    width: 800px;
    margin: 0;
    text-align: center;
    font-family: "Noto Serif", serif;
    font-size: 44px;
    font-weight: 400;
    color: var(--gold);
    letter-spacing: 0.5px;
  }
  .closing {
    position: absolute;
    left: 0;
    top: 893px;
    width: 800px;
    margin: 0;
    text-align: center;
    font-family: "Noto Serif", serif;
    font-size: 27px;
    line-height: 35px;
    color: var(--gold);
  }
</style>
</head>
<body>
<main class="invitation">
  <div class="henna-motif henna-motif--top-left" role="img" aria-label="Gold henna mandala with paisley and flower patterns"></div>

  <div class="garland garland--top" role="img" aria-label="Gold beaded strings with two hanging gold feathers"></div>

  <p class="script script--intro">
    With immense joy and love,<br>
    we invite you to celebrate the Henna Party<br>
    of our beloved niece
  </p>

  <div class="divider-mark" role="img" aria-label="Small gold flower ornament"></div>

  <h1 class="event-date">March 20, 2026</h1>

  <p class="script script--message">
    Join us as we adorn her hands with henna and<br>
    our hearts with happiness,<br>
    surrounded by family, culture, and timeless<br>
    traditions.
  </p>

  <p class="closing">
    Your presence<br>
    will make this evening even more special.
  </p>

  <div class="garland garland--bottom" role="img" aria-label="Gold beaded strings curving along the lower corner"></div>

  <div class="henna-motif henna-motif--bottom-right" role="img" aria-label="Gold henna mandala with swirling floral patterns"></div>
</main>
</body>
</html>
```